依頼詳細
残暑お見舞い申し上げます

コロナ禍と暑さで汗が噴き出るような日々が続きますが、いかがお過ごしでしょうか?
汗はかけばかくほど、老廃物が体内から出て、心も体も健康になります。
汗をかかないようにすることは、決して良いことではありません。
会社にとっても、今年は汗(特別損失)を出せるチャンスです。
個人も会社もたくさんの汗を出して、より健康体になられること、心より祈念申し上げます。

★写真に添える文章:松本清志の最新刊
「伸びる会社へ組み直す」
定価10,780円(税込み)
記載項目
ノルフェン・パートナーズ
松本 清志・長谷 宗一郎・柴田 昌平
希望イメージ
シンプル 複雑
単色 カラフル
暗い 明るい
日常 高級
遊び心 厳粛
未来的 伝統的
女性的 男性的
希望する色
水色系
納品ファイル
• 高解像度JPG (.jpg)
補足説明
■ 選んだ理由

今年はコロナのイベント中止で花火大会もなくなるなかで、
もってこいのデザインでした。
文字の並べ方に工夫が見られ、メッセージとバックのコントラストが素敵でした。
一目見ておしゃれで気に入りました。

■ 提案者全員のお礼・コメント

この度は、ご応募ありがとうございました。
毎回、新たなご提案が来るのが楽しみでした。素敵なご応募をありがとうございました。

```html
<!DOCTYPE html>
<html lang="ja">
<head>
<meta charset="utf-8">
<title>残暑お見舞い申し上げます</title>
<link rel="stylesheet" href="https://fonts.googleapis.com/css2?family=Noto+Serif+JP:wght@400;600;700&display=swap">
<style>
  :root {
    --paper: #ffffff;
    --ripple: #d6ecf8;
    --ripple-deep: #b9dcf2;
    --heading-blue: #3282c6;
    --text-grey: #5a5a5a;
    --accent-red: #c23a2b;
    --band-blue: #3f90d3;
    --fish-light: #f7b25a;
    --fish-deep: #e2521e;
    --book-light: #9e2a22;
    --book-deep: #4a120e;
  }
  * { margin: 0; padding: 0; box-sizing: border-box; }
  html, body { width: 885px; height: 1200px; overflow: hidden; }
  body {
    position: relative;
    background: var(--paper);
    font-family: "Noto Serif JP", serif;
    color: var(--text-grey);
  }
  .ripple {
    position: absolute;
    border-radius: 50%;
    background: radial-gradient(ellipse at center, var(--ripple-deep) 0%, var(--ripple) 45%, rgba(214,236,248,0) 72%);
  }
  .greeting-title {
    position: absolute;
    top: 80px;
    right: 48px;
    height: 380px;
    writing-mode: vertical-rl;
    font-size: 46px;
    font-weight: 700;
    line-height: 1.35;
    letter-spacing: 0.08em;
    color: var(--heading-blue);
  }
  .greeting-body {
    position: absolute;
    top: 92px;
    right: 218px;
    height: 320px;
    writing-mode: vertical-rl;
    font-size: 18px;
    line-height: 1.62;
    letter-spacing: 0.02em;
    z-index: 2;
  }
  .company-name {
    position: absolute;
    top: 86px;
    left: 40px;
    writing-mode: vertical-rl;
    font-size: 33px;
    font-weight: 700;
    letter-spacing: 0.06em;
    color: var(--heading-blue);
    z-index: 2;
  }
  .staff-names {
    position: absolute;
    top: 92px;
    left: 104px;
    writing-mode: vertical-rl;
    font-size: 15px;
    letter-spacing: 0.12em;
    z-index: 2;
  }
  .goldfish {
    position: absolute;
    border-radius: 50% 40% 55% 45%;
    background: radial-gradient(ellipse at 40% 40%, var(--fish-light) 0%, var(--fish-deep) 70%, rgba(226,82,30,0) 100%);
  }
  .book-cover {
    position: absolute;
    left: 292px;
    top: 500px;
    width: 250px;
    height: 470px;
    background: linear-gradient(160deg, var(--book-light) 0%, var(--book-deep) 100%);
    box-shadow: 6px 8px 14px rgba(0,0,0,0.25);
  }
  .new-release {
    position: absolute;
    left: 0; right: 0;
    top: 1036px;
    padding-left: 140px;
    text-align: center;
  }
  .new-release__lead {
    font-size: 28px;
    font-weight: 700;
    color: var(--accent-red);
    letter-spacing: 0.04em;
  }
  .new-release__title {
    display: inline-block;
    margin-top: 10px;
    padding: 8px 34px;
    background: var(--band-blue);
    color: #fff;
    font-size: 24px;
    font-weight: 600;
    letter-spacing: 0.06em;
  }
  .new-release__price {
    margin-top: 8px;
    font-size: 17px;
    color: var(--text-grey);
  }
</style>
</head>
<body>
  <div class="ripple" style="left:600px;top:30px;width:300px;height:200px;"></div>
  <div class="ripple" style="left:-80px;top:560px;width:360px;height:240px;"></div>
  <div class="ripple" style="left:470px;top:430px;width:330px;height:210px;"></div>
  <div class="ripple" style="left:560px;top:780px;width:340px;height:230px;"></div>
  <div class="ripple" style="left:60px;top:930px;width:300px;height:200px;"></div>
  <div class="ripple" style="left:250px;top:240px;width:260px;height:170px;"></div>

  <h1 class="greeting-title">残暑お見舞い<br>申し上げます</h1>

  <p class="greeting-body">
    コロナ禍と暑さで汗が噴き出るような日々が続きますが、いかがお過ごしでしょうか?<br>
    汗はかけばかくほど、老廃物が体内から出て、心も体も健康になります。<br>
    汗をかかないようにすることは、決して良いことではありません。<br>
    会社にとっても、今年は汗(特別損失)を出せるチャンスです。<br>
    個人も会社もたくさんの汗を出して、より健康体になられること、心より祈念申し上げます。
  </p>

  <p class="company-name">ノルフェン・パートナーズ</p>
  <p class="staff-names">松本 清志・長谷 宗一郎・柴田 昌平</p>

  <div class="goldfish" role="img" aria-label="泳ぐ金魚のイラスト" style="left:100px;top:430px;width:240px;height:270px;transform:rotate(-18deg);"></div>
  <div class="goldfish" role="img" aria-label="泳ぐ金魚のイラスト" style="left:560px;top:480px;width:200px;height:170px;transform:rotate(20deg);"></div>
  <div class="goldfish" role="img" aria-label="泳ぐ金魚のイラスト" style="left:670px;top:690px;width:180px;height:230px;transform:rotate(-12deg);"></div>

  <div class="book-cover" role="img" aria-label="新刊『伸びる会社へ組み直す』の表紙写真"></div>

  <div class="new-release">
    <p class="new-release__lead">松本清志の最新刊</p>
    <p class="new-release__title">伸びる会社へ組み直す</p>
    <p class="new-release__price">定価 10,780円（税込み）</p>
  </div>
</body>
</html>
```